Packaging Design - Diet Sachet Project

I am looking for a label to be printed on the side of a sachet for a diet shake. The size is 100x180mm label.
I would like the design to be in one colour, the blue that is in our company logo (#00c0ff). The design will be on a dull chrome colour sachet (you can utilize transparency). I have two variations of the logo attached, you can utilize either one how you wish.
I would like the label to portray the following messaging;
Main point: VLCD Meal Replacement
Sub messaging:
- Nutritionally Balanced
- Scientifically Based
- Highest Quality
- Great Tasting
- More Rapid Weight Loss Than Traditional Diets
- Supports Healthy Weight Loss
- Directions - put 200mls of cool water in a Shaker (or use a whisk), add contents of the sachet and shake or whisk vigorously for 30 seconds.
- Use shakes as a replacement for 3 of your 4 daily meals and consume a healthy low fat, low carb meal each day. For best results complete 20 minutes of exercise per day.
- For best before see back of sachet.
Please don't just use lots of bullet points on the design, try and put the messaging across in a more constructive way.
If some messaging needs to be left off to enhance design, then feel free but the design needs to portray those brand ideals.
Take a look at our website to see branding in action www.quillbernstowe.co.uk. Bare in mind it isn't great though and is due for re-design ;)
Any other questions please ask I don't mind.

```html
<!DOCTYPE html>
<html lang="en">
<head>
<meta charset="utf-8">
<title>Quill Bernstowe – French Vanilla Sachet Label</title>
<link rel="stylesheet" href="https://fonts.googleapis.com/css2?family=Mulish:wght@700;800&family=Arimo:wght@400;700&family=Source+Serif+4:wght@300&family=Roboto+Condensed:wght@400;700&display=swap">
<style>
  :root {
    --brand-blue: #3cbdee;
    --ink: #1e1e1e;
    --ink-soft: #444;
    --paper: #ffffff;
    --backdrop: #e4e5e7;
    --rule: #222;
    --rule-soft: #999;
  }
  * { box-sizing: border-box; margin: 0; padding: 0; }
  html, body { width: 1200px; height: 900px; overflow: hidden; }
  body {
    background: var(--backdrop);
    font-family: "Arimo", Arial, sans-serif;
    color: var(--ink);
    position: relative;
  }
  .label {
    position: absolute;
    top: 40px;
    width: 458px;
    height: 822px;
    background: var(--paper);
    border-radius: 18px;
    overflow: hidden;
  }
  .label--front { left: 52px; }
  .label--back { left: 690px; }

  /* Front */
  .brand-panel {
    position: absolute;
    left: 22px; top: 20px;
    width: 413px; height: 417px;
    background: var(--brand-blue);
    color: var(--paper);
    display: flex;
    flex-direction: column;
    align-items: center;
    justify-content: center;
    gap: 34px;
  }
  .brand-name {
    font-family: "Mulish", sans-serif;
    font-weight: 700;
    font-size: 54px;
    line-height: 1.05;
    text-align: center;
  }
  .brand-dot {
    width: 120px; height: 120px;
    border-radius: 50%;
    background: var(--paper);
  }
  .tagline {
    position: absolute;
    left: 0; top: 488px;
    width: 458px;
    text-align: center;
    font-family: "Mulish", sans-serif;
    font-weight: 800;
    font-size: 25px;
    line-height: 33px;
    color: var(--brand-blue);
    transform: rotate(-11deg);
    transform-origin: center;
    white-space: nowrap;
  }
  .flavour-badge {
    position: absolute;
    left: 285px; top: 655px;
    width: 150px; height: 150px;
    border-radius: 50%;
    background: var(--brand-blue);
    color: var(--paper);
    display: flex;
    align-items: center;
    justify-content: center;
    text-align: center;
    font-family: "Arimo", sans-serif;
    font-weight: 700;
    font-size: 23px;
    line-height: 1.3;
  }

  /* Back */
  .back-headline {
    position: absolute;
    left: 0; top: 8px; width: 458px;
    text-align: center;
    font-family: "Source Serif 4", serif;
    font-weight: 300;
    font-size: 22px;
    line-height: 1.22;
    color: var(--brand-blue);
  }
  .directions {
    position: absolute;
    left: 22px; top: 72px; width: 418px;
    font-size: 10.5px;
    font-weight: 700;
    line-height: 1.45;
  }
  .directions h2 { font-size: 11.5px; margin-bottom: 10px; }
  .directions p { margin-bottom: 14px; }
  .ingredients {
    position: absolute;
    left: 18px; top: 268px; width: 200px;
  }
  .ingredients h2 {
    text-align: center; font-size: 12px; font-weight: 700; margin-bottom: 14px;
  }
  .ingredients p { font-size: 8px; line-height: 1.4; color: var(--ink-soft); }
  .contact {
    position: absolute;
    left: 18px; top: 428px; width: 200px;
    text-align: center;
    font-weight: 700;
  }
  .contact address { font-style: normal; font-size: 11.5px; line-height: 1.3; }
  .contact .phone { font-size: 19px; margin-top: 20px; }
  .contact .email { font-size: 11px; margin-top: 2px; }
  .best-before {
    position: absolute;
    left: 26px; top: 690px;
    font-weight: 700; font-size: 12.5px;
  }
  .best-before p + p { margin-top: 21px; }

  .nutrition {
    position: absolute;
    left: 236px; top: 207px;
    width: 207px; height: 438px;
    border: 1px solid var(--rule);
    padding: 4px 6px;
    font-family: "Roboto Condensed", sans-serif;
    font-size: 8.6px;
    line-height: 13px;
  }
  .nutrition h2 { font-size: 12px; font-weight: 700; line-height: 15px; }
  .nf-row { display: grid; grid-template-columns: 95px 55px 1fr; height: 12px; line-height: 12px; }
  .nf-row--item { height: 14.4px; line-height: 14px; }
  .nf-row--sub { padding-left: 18px; grid-template-columns: 77px 55px 1fr; }
  .nf-row--line { border-bottom: 0.6px solid var(--rule-soft); }
  .nf-bold { font-weight: 700; }
  .nf-thick { border-bottom: 3px solid var(--rule); margin: 2px 0; }
  .nf-thin { border-bottom: 1px solid var(--rule); margin: 2px 0; }
  .nf-note { font-size: 8px; line-height: 10px; margin: 2px 0; }
  .nf-limits { display: grid; grid-template-columns: 56px 52px 40px 1fr; height: 14px; line-height: 14px; }
  .nf-limits--head { font-weight: 700; grid-template-columns: 108px 40px 1fr; }
  .nf-right { text-align: right; }
  .nf-gram { display: flex; justify-content: space-between; padding-right: 10px; font-weight: 700; line-height: 13px; }
</style>
</head>
<body>

<section class="label label--front">
  <div class="brand-panel">
    <div class="brand-name">Quill<br>Bernstowe</div>
    <div class="brand-dot" aria-hidden="true"></div>
  </div>
  <p class="tagline">Lose weight faster than<br>traditional diets with this<br>nutritionally balanced and<br>scientific blend of nutrients<br>that just happens to taste<br>great.</p>
  <div class="flavour-badge">French<br>Vanilla</div>
</section>

<section class="label label--back">
  <h1 class="back-headline">Now you can Quill Bernstowe in a<br>balanced, scientific and delicious way.</h1>

  <div class="directions">
    <h2>DIRECTIONS:</h2>
    <p>• Put 200mls of cool water in a Shaker (or use a whisk), add contents of the sachet and shake or whisk vigorously for 30 seconds.</p>
    <p>• Use shakes as a replacement for 3 of your 4 daily meals and consume a healthy low fat, low carb meal each day. For best results complete 20 minutes of exercise per day.</p>
  </div>

  <div class="ingredients">
    <h2>INGREDIENTS</h2>
    <p>Lorem ipsum dolor sit amet, pellentesque mauris ligula magna ut. Mauris duis pretium, vitae in ad viverra, dictum placerat. Turpis nunc. Vestibulum est cras, donec in suscipit, vitae ut feugiat.</p>
  </div>

  <div class="contact">
    <address>Quill Bernstowe<br>P.O. Box 517<br>Harwick, 40213</address>
    <p class="phone">1 888 555-0142</p>
    <p class="email">info@quillbernstowe.co.uk</p>
  </div>

  <div class="nutrition">
    <h2>Nutrition Facts</h2>
    <div class="nf-row"><span>Serving Size</span><span>1</span><span class="nf-right">100g</span></div>
    <div class="nf-row"><span>Servings Per Customer</span><span>&nbsp;&nbsp;1</span><span></span></div>
    <div class="nf-thick"></div>
    <div class="nf-bold">Amount Per Serving</div>
    <div class="nf-row nf-row--line"><span>Calories 41</span><span style="grid-column: span 2">Calories from Fat 15%</span></div>
    <div class="nf-right" style="line-height:12px">% Daily Value</div>
    <div class="nf-row nf-row--item nf-row--line"><span class="nf-bold">Toal Fat</span><span>0g</span><span>0%</span></div>
    <div class="nf-row nf-row--item nf-row--sub nf-row--line"><span>Saturated</span><span>0g</span><span>0%</span></div>
    <div class="nf-row nf-row--item nf-row--sub nf-row--line"><span>+Trans</span><span>0g</span><span>0%</span></div>
    <div class="nf-row nf-row--item nf-row--line"><span class="nf-bold">Cholesterol</span><span>0mg</span><span>0%</span></div>
    <div class="nf-row nf-row--item nf-row--line"><span class="nf-bold">Sodium</span><span>160mg</span><span>6%</span></div>
    <div class="nf-row nf-row--item nf-row--line"><span class="nf-bold">Total Carbohydrate</span><span>17g</span><span>6%</span></div>
    <div class="nf-row nf-row--item nf-row--sub nf-row--line"><span>Fibre</span><span>0g</span><span></span></div>
    <div class="nf-row nf-row--item nf-row--sub nf-row--line"><span>Sugars</span><span>6g</span><span></span></div>
    <div class="nf-row nf-row--item"><span class="nf-bold">Protein</span><span>.4g</span><span></span></div>
    <div class="nf-thick"></div>
    <div class="nf-row nf-row--item nf-row--line"><span class="nf-bold">Calcium</span><span>84mcg</span><span>0%</span></div>
    <div class="nf-row nf-row--item"><span class="nf-bold">Iron</span><span>1.8mg</span><span>2%</span></div>
    <div class="nf-thin"></div>
    <p class="nf-note">* Percent Daily Values are based on a 2,000 calorie diet. Most daily values may be higher or lower depending on your calorie needs.</p>
    <div class="nf-limits nf-limits--head"><span>&nbsp;&nbsp;&nbsp;Calories</span><span>2,000</span><span>2,500</span></div>
    <div class="nf-thin"></div>
    <div class="nf-limits"><span>Total Fat</span><span>Less than</span><span>0</span><span>0</span></div>
    <div class="nf-limits"><span>Sat Fat</span><span>Less than</span><span>0</span><span>0</span></div>
    <div class="nf-limits"><span>Cholesterol</span><span>Less than</span><span>0</span><span>0</span></div>
    <div class="nf-limits"><span>Sodium</span><span>Less than</span><span>0</span><span>0</span></div>
    <div class="nf-limits"><span style="grid-column: span 2">Total Carbohydrates</span><span>0</span><span>0</span></div>
    <div class="nf-limits"><span style="grid-column: span 2">Fiber</span><span>0</span><span>0</span></div>
    <div class="nf-thin"></div>
    <div class="nf-bold">Calories per gram</div>
    <div class="nf-gram"><span>Fat 0</span><span>Carbohydrates 4</span><span>Protein 4</span></div>
  </div>

  <div class="best-before">
    <p>BEST BEFORE:</p>
    <p>July 2017</p>
  </div>
</section>

</body>
</html>
```